ARC VOLLEY Business Card Project

I'd like to request a business card design for the new company I've launched.
The name of the company is "ARC VOLLEY" an indoor unmanned tennis practice facility.
We would like to see designs that use our brand identity color in the logo I've attached.
We hope to get the design with modern, luxurious and elegant tone and manner.
We hope the logo should not be too big.

Business card must have elements as below:
- Logo (One of the logos I've attached)
- Name (In Korean Text) : 박 서 윤
- Title (In Korean Text) : 대표
- Phone Number : 010-8472-3916
- Email Address : seoyun.park@arcvolley-example.co.kr
- Website : www.arcvolley-example.co.kr
- Instagram : arcvolley
- Address (In Korean text) : 경기도 용인시 수지구 풍덕천로 456 미래타워 5층 501호, 502호

Target Market(s)

Tennis amateurs in 20 to 40s

Industry/Entity Type

Sports, Hobby

Contact Information for Business Card

- Logo (One of the logos I've attached) - Name (In Korean Text) : 박 서 윤 - Title (In Korean Text) : 대표 - Phone Number : 010-8472-3916 - Email Address : seoyun.park@arcvolley-example.co.kr - Website : www.arcvolley-example.co.kr - Instagram : arcvolley - Address (In Korean text) : 경기도 용인시 수지구 풍덕천로 456 미래타워 5층 501호, 502호

Font styles to use
Sans Serif

Requirements
Must have
• Double sided
Nice to have
• Logo with intaglio or relief embossing
Should not have
• Logo should not be too big.

```html
<!DOCTYPE html>
<html lang="ko">
<head>
<meta charset="utf-8">
<title>ARC VOLLEY Business Card</title>
<link rel="stylesheet" href="https://fonts.googleapis.com/css2?family=Noto+Sans+KR:wght@400;700&family=Poppins:wght@300;400;500&display=swap">
<style>
  :root {
    --bg: #2a2b2a;
    --brand-green: #2f5e3f;
    --brand-green-light: #4a7d5a;
    --brand-green-dark: #24502f;
    --card-white: #f7f7f6;
    --ink: #3a3a3a;
    --muted: #555555;
    --rule: #5a5a5a;
  }
  * { box-sizing: border-box; margin: 0; padding: 0; }
  html, body { width: 1200px; height: 1200px; overflow: hidden; }
  body {
    background: var(--bg);
    font-family: "Poppins", "Noto Sans KR", sans-serif;
    display: flex;
    flex-direction: column;
    align-items: center;
    justify-content: center;
    gap: 60px;
  }
  .card {
    width: 800px;
    height: 457px;
    position: relative;
    overflow: hidden;
    box-shadow: 0 18px 40px rgba(0,0,0,0.45);
  }

  /* Back side */
  .card-back { background: var(--brand-green); }
  .card-back .pattern-field {
    position: absolute; inset: 0;
    background: radial-gradient(ellipse at 55% 45%, var(--brand-green-light) 0%, var(--brand-green) 55%, var(--brand-green-dark) 100%);
  }
  .card-back .brand-lockup {
    position: absolute; left: 50%; top: 50%;
    transform: translate(-50%, -50%);
    display: flex; align-items: center; gap: 16px;
    color: #ffffff;
  }
  .brand-mark {
    width: 44px; height: 44px; border-radius: 50%;
    border: 3px solid currentColor;
    flex: none;
  }
  .brand-name {
    font-family: "Poppins", sans-serif;
    font-weight: 500;
    font-size: 40px;
    letter-spacing: 3px;
    white-space: nowrap;
  }

  /* Front side */
  .card-front { background: linear-gradient(135deg, #fbfbfb 0%, var(--card-white) 60%, #eeeeec 100%); }
  .card-front .brand-lockup {
    position: absolute; left: 48px; top: 50%;
    transform: translateY(-50%);
    display: flex; align-items: center; gap: 12px;
    color: var(--brand-green);
  }
  .card-front .brand-mark { width: 48px; height: 48px; }
  .card-front .brand-name { font-size: 30px; letter-spacing: 2px; }
  .divider {
    position: absolute; left: 392px; top: 78px;
    width: 2px; height: 300px;
    background: var(--rule);
  }
  .person {
    position: absolute; left: 428px; top: 66px;
    width: 350px;
  }
  .person-name {
    font-family: "Noto Sans KR", sans-serif;
    font-weight: 700;
    font-size: 40px;
    line-height: 1.2;
    color: var(--brand-green);
    letter-spacing: 4px;
  }
  .person-title {
    font-family: "Noto Sans KR", sans-serif;
    font-size: 18px;
    color: var(--muted);
    margin-top: 2px;
  }
  .contact-list {
    list-style: none;
    margin-top: 30px;
    font-family: "Poppins", "Noto Sans KR", sans-serif;
    font-size: 15px;
    font-weight: 300;
    color: var(--ink);
    line-height: 1.5;
    display: flex;
    flex-direction: column;
    gap: 6px;
  }
  .contact-list li { display: flex; align-items: flex-start; gap: 10px; white-space: nowrap; }
  .contact-list li.address { white-space: normal; font-family: "Noto Sans KR", sans-serif; font-size: 14px; }
  .contact-list svg { width: 15px; height: 15px; flex: none; margin-top: 4px; }
  .contact-list .icon-fill { fill: var(--brand-green); }
  .contact-list .icon-line { fill: none; stroke: var(--brand-green); stroke-width: 2; }
</style>
</head>
<body>
  <section class="card card-back" aria-label="Business card back">
    <div class="pattern-field" role="img" aria-label="Embossed repeating brand pattern on green"></div>
    <div class="brand-lockup">
      <span class="brand-mark"></span>
      <span class="brand-name">ARC VOLLEY</span>
    </div>
  </section>

  <section class="card card-front" aria-label="Business card front">
    <div class="brand-lockup">
      <span class="brand-mark"></span>
      <span class="brand-name">ARC VOLLEY</span>
    </div>
    <div class="divider"></div>
    <div class="person">
      <p class="person-name">박 서 윤</p>
      <p class="person-title">대표</p>
      <ul class="contact-list">
        <li>
          <svg viewBox="0 0 24 24" aria-hidden="true"><path class="icon-fill" d="M6.6 10.8a15.1 15.1 0 0 0 6.6 6.6l2.2-2.2a1 1 0 0 1 1-.25 11.4 11.4 0 0 0 3.6.57 1 1 0 0 1 1 1V20a1 1 0 0 1-1 1A17 17 0 0 1 3 4a1 1 0 0 1 1-1h3.5a1 1 0 0 1 1 1c0 1.25.2 2.45.57 3.57a1 1 0 0 1-.25 1z"/></svg>
          <span>010-8472-3916</span>
        </li>
        <li>
          <svg viewBox="0 0 24 24" aria-hidden="true"><path class="icon-fill" d="M2 5h20v14H2z"/><path d="M2 6l10 7 10-7" fill="none" stroke="#ffffff" stroke-width="1.6"/></svg>
          <span>seoyun.park@arcvolley-example.co.kr</span>
        </li>
        <li>
          <svg viewBox="0 0 24 24" aria-hidden="true"><circle class="icon-line" cx="12" cy="12" r="9"/><path class="icon-line" d="M3 12h18M12 3c3 3 3 15 0 18M12 3c-3 3-3 15 0 18"/></svg>
          <span>www.arcvolley-example.co.kr</span>
        </li>
        <li>
          <svg viewBox="0 0 24 24" aria-hidden="true"><rect class="icon-line" x="4" y="4" width="16" height="16" rx="4"/></svg>
          <span>arcvolley</span>
        </li>
        <li class="address">
          <svg viewBox="0 0 24 24" aria-hidden="true"><path class="icon-fill" d="M12 2a7 7 0 0 0-7 7c0 5 7 13 7 13s7-8 7-13a7 7 0 0 0-7-7zm0 9.5A2.5 2.5 0 1 1 12 6.5a2.5 2.5 0 0 1 0 5z"/></svg>
          <span>경기도 용인시 수지구 풍덕천로 456 미래타워 5층 501호, 502호</span>
        </li>
      </ul>
    </div>
  </section>
</body>
</html>
```